We need a business card design for a new brand within our existing financial marketing business. Our new brand is www.qalvenport.co.uk

We attach various logo files - please use the version that will produce the sharpest image on the business card.

We are flexible about shape of card etc. Please think outside the box as to what goes on front and what goes on back of the card.

The card needs to be corporate, but really catch the eye ( e.g. premium translucent cards on plastic etc or metal cards or shiny surface etc )

We want to be able to amend the card (once the design has been agreed ) to add additional staff details, but the text to go on it will be generic

Details to go on card ( for the first generic one) are fairly minimal as we don't like cluttered business cards:-

Owen Tagget
Managing Director

Mobile: 07852 418 207
Email: o.tagget@qalvenport.co.uk

Financial

```html
<!DOCTYPE html>
<html lang="en">
<head>
<meta charset="utf-8">
<title>Qalvenport business card</title>
<link rel="stylesheet" href="https://fonts.googleapis.com/css2?family=Oswald:wght@500&family=Quicksand:wght@500&display=swap">
<style>
  :root {
    --brand-blue: #1b77c0;
    --brand-yellow: #dcb42b;
    --card-white: #ffffff;
    --edge-grey: #8d9196;
    --stage: #e4e6e9;
    --text-white: #ffffff;
  }
  * { margin: 0; padding: 0; box-sizing: border-box; }
  html, body {
    width: 1200px; height: 892px; overflow: hidden;
    background: var(--stage);
    font-family: "Quicksand", sans-serif;
  }
  .canvas {
    position: relative; width: 1200px; height: 892px;
    display: flex; flex-direction: column; align-items: center; justify-content: center; gap: 32px;
  }
  .card {
    position: relative; width: 700px; height: 400px;
    background: var(--card-white);
    box-shadow: 0 6px 18px rgba(0,0,0,0.18);
    overflow: hidden;
  }
  .brand {
    position: absolute;
    color: var(--brand-blue);
    font-family: "Oswald", sans-serif; font-weight: 500;
    text-transform: uppercase; letter-spacing: 6px; line-height: 1;
    white-space: nowrap;
  }
  .card-front .brand { left: 50%; top: 50%; transform: translate(-50%, -50%); font-size: 52px; }
  .card-back .brand { left: 396px; top: 58px; font-size: 36px; letter-spacing: 4px; }
  .back-shapes { position: absolute; inset: 0; }
  .person { position: absolute; left: 36px; top: 262px; color: var(--brand-yellow); }
  .person-name { font-family: "Oswald", sans-serif; font-weight: 500; font-size: 30px; letter-spacing: 1px; line-height: 1; }
  .person-role { font-family: "Oswald", sans-serif; font-weight: 500; font-size: 14px; letter-spacing: 2px; margin-top: 6px; }
  .contacts { position: absolute; left: 384px; top: 196px; list-style: none; color: var(--text-white); font-size: 11.5px; font-weight: 500; line-height: 1.35; }
  .contact { display: flex; align-items: center; gap: 12px; margin-bottom: 10px; }
  .contact-icon { width: 24px; height: 24px; flex: none; }
</style>
</head>
<body>
<main class="canvas">
  <section class="card card-front" aria-label="Card front">
    <p class="brand">Qalvenport</p>
  </section>

  <section class="card card-back" aria-label="Card back">
    <svg class="back-shapes" viewBox="0 0 700 400" width="700" height="400" aria-hidden="true">
      <rect width="700" height="400" fill="var(--brand-blue)"/>
      <polygon points="230,0 700,0 700,100 290,190" fill="var(--card-white)"/>
      <polyline points="230,0 290,190 700,100" fill="none" stroke="var(--edge-grey)" stroke-width="3"/>
      <polygon points="290,190 700,100 700,300 250,390" fill="var(--brand-yellow)"/>
      <polygon points="0,135 110,135 340,250 160,400 0,400" fill="var(--card-white)"/>
      <polyline points="110,135 340,250 160,400" fill="none" stroke="var(--edge-grey)" stroke-width="3"/>
    </svg>

    <p class="brand">Qalvenport</p>

    <div class="person">
      <p class="person-name">OWEN TAGGET</p>
      <p class="person-role">GENERAL MANAGER</p>
    </div>

    <ul class="contacts">
      <li class="contact">
        <svg class="contact-icon" viewBox="0 0 24 24" aria-hidden="true">
          <circle cx="12" cy="12" r="12" fill="var(--card-white)"/>
          <path d="M6 12 L12 6.5 L18 12 H16 V17.5 H13.5 V14 H10.5 V17.5 H8 V12 Z" fill="var(--brand-yellow)"/>
        </svg>
        <span>14 Harrow Lane,<br>2nd Floor West</span>
      </li>
      <li class="contact">
        <svg class="contact-icon" viewBox="0 0 24 24" aria-hidden="true">
          <circle cx="12" cy="12" r="12" fill="var(--card-white)"/>
          <rect x="8.5" y="5" width="7" height="14" rx="1.5" fill="var(--brand-yellow)"/>
          <rect x="9.8" y="7" width="4.4" height="8.5" fill="var(--card-white)"/>
        </svg>
        <span>07852 418 207</span>
      </li>
      <li class="contact">
        <svg class="contact-icon" viewBox="0 0 24 24" aria-hidden="true">
          <circle cx="12" cy="12" r="12" fill="var(--card-white)"/>
          <g fill="none" stroke="var(--brand-yellow)" stroke-width="1.5">
            <circle cx="12" cy="12" r="6"/>
            <ellipse cx="12" cy="12" rx="2.6" ry="6"/>
            <line x1="6" y1="12" x2="18" y2="12"/>
          </g>
        </svg>
        <span>o.tagget@qalvenport.co.uk<br>www.qalvenport.co.uk</span>
      </li>
    </ul>
  </section>
</main>
</body>
</html>
```